Portfolio site - Need a basic WordPress or SquareSpace site

I need a portfolio site where I have the option to keep updating it on my own. Therefore, I'm guessing I need one that uses WordPress or SquareSpace. I just need a simple and elegant design. I'm a writer (scholarly, fiction and journalism).

Target Market(s)

Adult

Industry/Entity Type

Writer

Number of Pages Required

4 page

Font styles to use
Serif

Colors
b7a5cd
e667a6
85abd2

Requirements
Must have
• Easily updatable features. I'll have to publish links and small blurbs from time to time. And maybe the occasional image.
• Pages should be:
• Home
• Work
• Press
• Contact

```html
<!DOCTYPE html>
<html lang="en">
<head>
<meta charset="utf-8">
<title>Odessa Whitcombe – Writer</title>
<link rel="stylesheet" href="https://fonts.googleapis.com/css2?family=Poppins:wght@500;600&family=Lato:wght@400;700&display=swap">
<style>
:root{
  --accent:#85abd2;
  --accent-text:#7ea3cd;
  --ink:#111;
  --body:#555;
  --white:#fff;
  --rule:#dcdcdc;
  --frame-light:#d9e5f1;
}
*{box-sizing:border-box;margin:0;padding:0}
html,body{width:1200px;height:2344px;overflow:hidden}
body{position:relative;background:var(--white);font-family:'Lato',sans-serif;color:var(--body)}
.abs{position:absolute}
a{color:inherit}

/* header */
.brand{left:78px;top:30px;font-family:'Lato',sans-serif;font-weight:700;font-size:24px;color:var(--ink);letter-spacing:.5px}
.header-phone{right:82px;top:33px;font-size:16px;color:#444;display:flex;align-items:center;gap:22px}
.header-rule{left:78px;top:94px;width:1045px;height:1px;background:var(--rule)}
.main-nav{left:80px;top:107px;display:flex;font-size:15px;color:#555}
.main-nav a{text-decoration:none;width:108px}
.main-nav a.current{color:var(--accent-text)}
.search{left:1087px;top:103px;width:35px;height:35px;border-radius:50%;background:var(--accent)}

/* hero */
.hero{left:0;top:145px;width:1200px;height:574px;background:linear-gradient(110deg,#3a3a3a 0%,#262626 45%,#1e1e1e 100%)}
.hero-title{left:80px;top:280px;font-family:'Poppins',sans-serif;font-weight:600;font-size:42px;color:var(--white)}
.hero-title span,.accent{color:var(--accent-text)}
.hero-text{left:80px;top:363px;width:400px;font-size:15.5px;line-height:26px;color:var(--white)}
.btn{display:flex;align-items:center;justify-content:center;background:var(--accent);color:var(--white);font-family:'Poppins',sans-serif;font-weight:500;border-radius:3px;text-decoration:none}
.hero-btn{left:78px;top:523px;width:155px;height:50px;font-size:18px;border:1px solid #cfdff0}
.hero-social{left:670px;top:216px;display:flex;flex-direction:column;gap:18px}
.hero-social span{width:12px;height:12px;border-radius:2px;background:var(--accent)}
.hero-frame{left:703px;top:214px;width:375px;height:434px;border:22px solid #4b5563}
.hero-portrait{left:747px;top:148px;width:297px;height:474px;background:linear-gradient(180deg,#8a6b55 0%,#d9cbbd 45%,#c9bcb0 100%)}

/* about */
.about-frame{left:137px;top:781px;width:230px;height:266px;border:12px solid var(--frame-light)}
.about-book{left:200px;top:805px;width:184px;height:289px;background:linear-gradient(160deg,#1f4f5a 0%,#9b3b2c 50%,#d9a24a 100%);box-shadow:4px 6px 10px rgba(0,0,0,.3)}
.section-title{font-family:'Poppins',sans-serif;font-weight:600;font-size:37px;color:var(--ink)}
.about-title{left:509px;top:773px}
.about-text{left:509px;top:842px;width:612px;font-size:15.5px;line-height:26px}
.about-link{left:509px;top:987px;font-family:'Poppins',sans-serif;font-weight:500;font-size:15px;color:var(--accent-text);text-decoration:underline}
.about-btn{left:508px;top:1042px;width:145px;height:52px;font-size:17px}

/* reading band */
.band-photo{left:0;top:1156px;width:600px;height:333px;background:linear-gradient(120deg,#3c3c3c,#565656 60%,#444)}
.band-text{left:80px;top:1230px;width:400px;font-size:15.5px;line-height:26px;color:var(--white)}
.band-shelf{left:600px;top:1156px;width:600px;height:333px;background:var(--accent)}
.cover{top:1219px;width:136px;height:208px}
.cover-1{left:653px;background:linear-gradient(180deg,#6a4a2e,#2f4f7a)}
.cover-2{left:820px;background:linear-gradient(180deg,#2e5d8c,#e08a3a 70%,#3b2a1a)}
.cover-3{left:988px;background:linear-gradient(180deg,#3a3a3a,#1c1c1c)}
.shelf-arrows{left:1133px;top:1374px}

/* news */
.news-title{left:0;top:1545px;width:1200px;text-align:center}
.news-photo{top:1614px;width:322px;height:208px}
.news-photo-1{left:78px;background:linear-gradient(135deg,#e8e8e8,#9a9a9a)}
.news-photo-2{left:439px;background:linear-gradient(135deg,#6b4a2e,#b08a5a)}
.news-photo-3{left:802px;background:linear-gradient(135deg,#b9786a,#d8c2b0)}
.news-date{top:1614px;width:52px;height:54px;background:var(--accent);color:var(--white);font-family:'Poppins',sans-serif;text-align:center;line-height:1}
.news-date b{display:block;font-size:25px;font-weight:600;margin-top:4px}
.news-date small{font-size:14px}
.news-card{top:1802px;width:290px;height:187px;background:var(--white);box-shadow:0 4px 14px rgba(0,0,0,.12);padding:22px 26px 22px 23px}
.news-card h3{font-family:'Poppins',sans-serif;font-weight:500;font-size:16px;line-height:26px;color:var(--accent-text);margin-bottom:10px}
.news-card p{font-size:15px;line-height:26px}
.news-card p a{color:var(--accent-text)}

/* footer */
.footer{left:0;top:2063px;width:1200px;height:281px;background:var(--accent)}
.footer-head{font-family:'Poppins',sans-serif;font-weight:500;font-size:18px;color:var(--ink)}
.sitemap{left:80px;top:2092px;color:var(--white)}
.sitemap ul{list-style:none;margin-top:16px;font-size:15px;line-height:31px}
.touch{left:441px;top:2092px;color:var(--white)}
.touch-row{display:flex;align-items:center;gap:20px;font-size:15px;margin-top:20px}
.footer-blurb{left:810px;top:2090px;width:304px;text-align:center;font-size:15px;line-height:26px;color:var(--white)}
.footer-social{left:881px;top:2219px;display:flex;gap:8px}
.footer-social span{width:34px;height:34px;border-radius:50%;border:1px solid var(--white);display:flex;align-items:center;justify-content:center}
.footer-social span:first-child{background:var(--white)}
.footer-social i{width:10px;height:10px;border-radius:2px;background:var(--white)}
.footer-social span:first-child i{background:var(--accent)}
.footer-rule{left:78px;top:2281px;width:1045px;height:1px;background:rgba(255,255,255,.8)}
.copyright{left:0;top:2300px;width:1200px;text-align:center;font-size:14px;color:var(--white)}
.copyright b{font-weight:700}
</style>
</head>
<body>

<header>
  <div class="abs brand">Odessa Whitcombe</div>
  <div class="abs header-phone">
    <svg width="20" height="20" viewBox="0 0 24 24"><path fill="#85abd2" d="M6.6 10.8a15 15 0 0 0 6.6 6.6l2.2-2.2a1 1 0 0 1 1-.25 11.4 11.4 0 0 0 3.6.57 1 1 0 0 1 1 1V20a1 1 0 0 1-1 1A17 17 0 0 1 3 4a1 1 0 0 1 1-1h3.5a1 1 0 0 1 1 1c0 1.25.2 2.45.57 3.6a1 1 0 0 1-.25 1z"/></svg>
    555 010 2030
  </div>
  <div class="abs header-rule"></div>
  <nav class="abs main-nav">
    <a class="current" href="#">Home</a><a href="#">Work</a><a href="#">Press</a><a href="#">Contact</a>
  </nav>
  <div class="abs search">
    <svg width="35" height="35" viewBox="0 0 35 35"><circle cx="16" cy="16" r="6" fill="none" stroke="#fff" stroke-width="2.5"/><line x1="20.5" y1="20.5" x2="25" y2="25" stroke="#fff" stroke-width="3" stroke-linecap="round"/></svg>
  </div>
</header>

<section>
  <div class="abs hero" role="img" aria-label="Background photo of a hand writing in an open notebook on a desk"></div>
  <h1 class="abs hero-title">Hi, I'm <span>Odessa Whitcombe</span></h1>
  <p class="abs hero-text">Lorem Ipsum is simply dummy text of the printing and typesetting industry. Lorem Ipsum has been the industry's standard dummy text ever since the 1500s, when an unknown printer took a galley of type and scrambled it to make a type specimen book.</p>
  <a class="abs btn hero-btn" href="#">Contact Now!</a>
  <div class="abs hero-social"><span></span><span></span><span></span><span></span></div>
  <div class="abs hero-frame"></div>
  <div class="abs hero-portrait" role="img" aria-label="Portrait of the writer holding a pen and a tablet"></div>
</section>

<section>
  <div class="abs about-frame"></div>
  <div class="abs about-book" role="img" aria-label="Cover of the writer's published anthology"></div>
  <h2 class="abs section-title about-title">About <span class="accent">Me</span></h2>
  <p class="abs about-text">Lorem Ipsum is simply dummy text of the printing and typesetting industry. Lorem Ipsum has been the industry's standard dummy text ever since the 1500s, when an unknown printer took a galley of type and scrambled it to make a type specimen book. It has survived not only five centuries, but also the leap into electronic typesetting, remaining essentially unchanged.</p>
  <a class="abs about-link" href="#">Harbour Lights on Northpage</a>
  <a class="abs btn about-btn" href="#">Learn More</a>
</section>

<section>
  <div class="abs band-photo" role="img" aria-label="Photo of a writer's desk with notebook and plant"></div>
  <p class="abs band-text">Lorem Ipsum is simply dummy text of the printing and typesetting industry. Lorem Ipsum has been the industry's standard dummy text ever since the 1500s, when an unknown printer took a galley of type and scrambled it to make a type specimen book. It has survived not only five centuries, but also the leap into electronic typesetting, remaining essentially unchanged.</p>
  <div class="abs band-shelf"></div>
  <div class="abs cover cover-1" role="img" aria-label="Book cover"></div>
  <div class="abs cover cover-2" role="img" aria-label="Book cover"></div>
  <div class="abs cover cover-3" role="img" aria-label="Book cover"></div>
  <svg class="abs shelf-arrows" width="14" height="48" viewBox="0 0 14 48"><path d="M10 3 4 9l6 6" fill="none" stroke="#fff" stroke-width="2"/><path d="M4 33l6 6-6 6" fill="none" stroke="#fff" stroke-width="2"/></svg>
</section>

<section>
  <h2 class="abs section-title news-title">Latest <span class="accent">News</span></h2>

  <div class="abs news-photo news-photo-1" role="img" aria-label="Photo of a laptop on a busy work table"></div>
  <div class="abs news-date" style="left:98px"><b>24</b><small>Apr</small></div>
  <article class="abs news-card" style="left:94px"><h3>Lorem Ipsum is simply dummy text of the printing</h3><p>Lorem Ipsum is simply dummy text of the printing and typesetting industry....<a href="#">Read More</a></p></article>

  <div class="abs news-photo news-photo-2" role="img" aria-label="Photo of a woman writing in a library"></div>
  <div class="abs news-date" style="left:459px"><b>24</b><small>Apr</small></div>
  <article class="abs news-card" style="left:455px"><h3>Lorem Ipsum is simply dummy text of the printing</h3><p>Lorem Ipsum is simply dummy text of the printing and typesetting industry....<a href="#">Read More</a></p></article>

  <div class="abs news-photo news-photo-3" role="img" aria-label="Photo of a woman reading on a tablet outdoors"></div>
  <div class="abs news-date" style="left:822px"><b>24</b><small>Apr</small></div>
  <article class="abs news-card" style="left:818px"><h3>Lorem Ipsum is simply dummy text of the printing</h3><p>Lorem Ipsum is simply dummy text of the printing and typesetting industry....<a href="#">Read More</a></p></article>
</section>

<footer>
  <div class="abs footer"></div>
  <div class="abs sitemap">
    <div class="footer-head">Site Map</div>
    <ul><li>Home</li><li>Work</li><li>Press</li><li>Contact</li></ul>
  </div>
  <div class="abs touch">
    <div class="footer-head">Get In Touch</div>
    <div class="touch-row">
      <svg width="20" height="20" viewBox="0 0 24 24"><path fill="#111" d="M6.6 10.8a15 15 0 0 0 6.6 6.6l2.2-2.2a1 1 0 0 1 1-.25 11.4 11.4 0 0 0 3.6.57 1 1 0 0 1 1 1V20a1 1 0 0 1-1 1A17 17 0 0 1 3 4a1 1 0 0 1 1-1h3.5a1 1 0 0 1 1 1c0 1.25.2 2.45.57 3.6a1 1 0 0 1-.25 1z"/></svg>
      555 010 2030
    </div>
    <div class="touch-row" style="margin-top:28px">
      <svg width="20" height="16" viewBox="0 0 20 16"><rect x="1" y="1" width="18" height="14" fill="none" stroke="#111" stroke-width="2"/><path d="M1 1l9 8 9-8" fill="none" stroke="#111" stroke-width="2"/></svg>
      me@odessawhitcombe.com
    </div>
  </div>
  <p class="abs footer-blurb">Lorem Ipsum is simply dummy text of the printing and typesetting industry. Lorem Ipsum has been the industry's standard dummy text ever since</p>
  <div class="abs footer-social"><span><i></i></span><span><i></i></span><span><i></i></span><span><i></i></span></div>
  <div class="abs footer-rule"></div>
  <p class="abs copyright"><b>© ODESSA WHITCOMBE - 2018.</b> All Rights Reserved.</p>
</footer>

</body>
</html>
```